Letterhead Design

We need a new Letterhead design for a 30 year old Electrical Company. We service domestic and commercial places. We have a logo recently made so to incorporate that. Using same colours or interested to see others added.
Would like to see a couple of options with all the info in letterhead, then another with info in a footnote down the bottom.

info needed to be added:

-Lic. No 48162
8/22-24 Larkin Rd, Tolvern 2087
W - brightcoilpower.com.au
T - (02) 9471 3825
M - 0427 593 168
E - info@brightcoilpower.com.au
ABN: 42 597 214 630

Electrical

```html
<!DOCTYPE html>
<html lang="en">
<head>
<meta charset="utf-8">
<title>Brightcoil Power – Letterhead &amp; Folder</title>
<link rel="stylesheet" href="https://fonts.googleapis.com/css2?family=Didact+Gothic&family=Libre+Baskerville:wght@400;700&display=swap">
<style>
  :root {
    --bg-top: #eef1f3;
    --bg-bottom: #dde2e6;
    --paper: #ffffff;
    --ink: #2b2b2b;
    --ink-soft: #3a3a3a;
    --brand-dark: #1f3a3a;
    --orange: #ff9414;
    --orange-light: #ffa625;
    --orange-deep: #ff8510;
  }
  * { box-sizing: border-box; margin: 0; padding: 0; }
  html, body { width: 1200px; height: 784px; overflow: hidden; }
  body {
    position: relative;
    background: linear-gradient(180deg, var(--bg-top), var(--bg-bottom));
    font-family: "Didact Gothic", "Century Gothic", sans-serif;
    color: var(--ink);
  }
  .sheet {
    position: absolute;
    top: 45px;
    width: 513px;
    height: 696px;
    border-radius: 14px;
    box-shadow: 0 2px 6px rgba(0,0,0,0.18);
    overflow: hidden;
  }
  .letterhead { left: 42px; background: var(--paper); }
  .folder {
    left: 634px;
    background: linear-gradient(160deg, var(--orange-light) 0%, var(--orange) 55%, var(--orange-deep) 100%);
  }

  .brand-name {
    font-family: "Libre Baskerville", Georgia, serif;
    font-weight: 400;
    color: var(--brand-dark);
    display: flex;
    align-items: center;
    gap: 8px;
    white-space: nowrap;
  }
  .brand-mark { width: 12px; height: 12px; background: var(--orange); flex: none; }
  .letterhead .brand-name { position: absolute; left: 52px; top: 44px; font-size: 24px; }
  .folder .brand-name { position: absolute; left: 120px; top: 520px; font-size: 32px; color: var(--ink); }
  .folder .brand-mark { width: 16px; height: 16px; background: var(--ink); }
  .brand-rule { position: absolute; height: 1.5px; background: var(--orange); }
  .letterhead .brand-rule { left: 52px; top: 86px; width: 170px; }
  .folder .brand-rule { left: 124px; top: 591px; width: 270px; background: var(--ink); }

  .contact {
    position: absolute;
    right: 34px;
    top: 43px;
    list-style: none;
    font-family: "Libre Baskerville", Georgia, serif;
    font-size: 7.5px;
    line-height: 14px;
    color: var(--ink-soft);
    text-align: right;
  }
  .contact li { display: flex; justify-content: flex-end; align-items: center; gap: 4px; }
  .contact svg { width: 9px; height: 9px; fill: var(--orange); }

  .letter-body {
    position: absolute;
    left: 50px;
    top: 148px;
    width: 421px;
    font-size: 10.6px;
    line-height: 17.5px;
    text-align: justify;
    hyphens: auto;
    color: var(--ink);
  }
  .letter-body p + p { margin-top: 17.5px; }

  .signature { position: absolute; left: 383px; top: 584px; }
  .signature .name { font-size: 14px; color: var(--ink); }
  .signature .role { font-size: 10px; margin-top: 6px; }

  .footer-line {
    position: absolute;
    top: 655px;
    font-family: "Libre Baskerville", Georgia, serif;
    font-weight: 700;
    font-size: 6.5px;
    color: var(--orange);
  }
  .footer-abn { left: 50px; }
  .footer-address { right: 42px; }
  .footer-band {
    position: absolute;
    left: 0; right: 0; bottom: 0;
    height: 23px;
    background: var(--orange);
    color: #fff;
    font-family: "Libre Baskerville", Georgia, serif;
    font-weight: 700;
    font-size: 6.5px;
    letter-spacing: 2.6px;
    text-align: center;
    line-height: 25px;
  }

  .folder-pocket { position: absolute; right: 0; top: 150px; width: 40px; height: 220px; }
</style>
</head>
<body>
  <section class="sheet letterhead" aria-label="Letterhead">
    <div class="brand-name"><span class="brand-mark"></span>Brightcoil Power</div>
    <div class="brand-rule"></div>

    <ul class="contact">
      <li>(02) 9471 3825
        <svg viewBox="0 0 24 24" aria-hidden="true"><path d="M6.6 10.8a15.1 15.1 0 0 0 6.6 6.6l2.2-2.2c.3-.3.7-.4 1-.2 1.1.4 2.3.6 3.6.6.6 0 1 .4 1 1V20c0 .6-.4 1-1 1A17 17 0 0 1 3 4c0-.6.4-1 1-1h3.5c.6 0 1 .4 1 1 0 1.3.2 2.5.6 3.6.1.3 0 .7-.2 1z"/></svg>
      </li>
      <li>0427 593 168
        <svg viewBox="0 0 24 24" aria-hidden="true"><path d="M7 1h10a2 2 0 0 1 2 2v18a2 2 0 0 1-2 2H7a2 2 0 0 1-2-2V3a2 2 0 0 1 2-2zm0 3v14h10V4z"/></svg>
      </li>
      <li>info@brightcoilpower.com.au
        <svg viewBox="0 0 24 24" aria-hidden="true"><path d="M2 4h20v16H2zm2 2v.5l8 5 8-5V6z"/></svg>
      </li>
    </ul>

    <div class="letter-body">
      <p>Lorem ipsum dolor sit amet, consectetur adipiscing elit. Donec orci purus, luctus vitae dignissim eu, iaculis sed purus. Vivamus faucibus, ipsum nec aliquet viverra, leo mauris condimentum ligula, sit amet sagittis enim ligula quis arcu. Nam egestas tortor id nisi porttitor mattis. In tortor ante, ultricies in suscipit a, tempus non massa. Vivamus et auctor mi. Fusce vel massa nulla. Phasellus nec eros mauris, et scelerisque orci. Donec malesuada orci vitae nulla accumsan porta a id massa.</p>
      <p>Quisque accumsan iaculis magna sit amet fringilla. Maecenas consequat, magna eget tincidunt semper, odio nibh rutrum mi, id feugiat ante nisi eu risus. Vestibulum nunc orci, rhoncus a placerat in, ultricies in mi. Cras mattis varius eros, vel fringilla nisi suscipit eget. Quisque scelerisque sagittis nulla at porttitor. Mauris a justo et tellus interdum tristique. Sed id augue vitae urna euismod commodo aliquet a quam. Pellentesque arcu velit, cursus et malesuada ut, consequat et diam. Nullam erat sem, rhoncus id ullamcorper vitae, rhoncus et arcu. In ultricies ultricies nulla.</p>
      <p>Kut rutrum nisi iaculis at. Donec eu magna a metus ornare faucibus. Fusce aliquet faucibus ultricies. Morbi semper, est id tincidunt gravida, sem arcu adipiscing lacus, ac bibendum nulla leo eu purus. Quisque nec diam sed risus consectetur a ccumsan quis quis nibh. Vestibulum id purus lorem. Donec eu magna a metus ornare faucibus. Fusce aliquet faucibus ultricies. Morbi semper, est id tincidunt gravida, sem arcu adipiscing lacus, ac bibendum nulla leo eu purus. Quisque nec diam sed risus consectetur a ccumsan quis quis nibh. Vestibulum id purus lorem.</p>
    </div>

    <div class="signature">
      <div class="name">Owen Halloway</div>
      <div class="role">Co-Founder &amp; CEO</div>
    </div>

    <div class="footer-line footer-abn">ABN: 42 597 214 630</div>
    <div class="footer-line footer-address">8/22-24 Larkin Rd, Tolvern 2087</div>
    <div class="footer-band">www.brightcoilpower.com.au</div>
  </section>

  <section class="sheet folder" aria-label="Presentation folder">
    <svg class="folder-pocket" viewBox="0 0 40 220" aria-hidden="true">
      <path d="M40 0 C22 8 8 10 8 30 V220 H40 Z" fill="#ff8a12" opacity="0.55"/>
    </svg>
    <div class="brand-name"><span class="brand-mark"></span>Brightcoil Power</div>
    <div class="brand-rule"></div>
  </section>
</body>
</html>
```